Electrical Contracting Business card design

I would like a business card design for a new electrical business. I would like the print R.MOLT ELECTRICAL in large block lettering (spot gloss) on the front with atoms flying in a circle around the letter "A" of R.MOLT. Dark blue background, red lettering with the southern cross stars splashed in between the background and lettering.

On the rear of the card I would like the centre to have a box with 2 or 3 lines in it ( a space to write a time and date for the job to take place) surrounded by a big mass of confusing looking cables or a circuit diagram (something that would overwhelm people trying to make sense of it).

Thank you, I hope this isn't to detailed

Industry/Entity Type

Electrical

Contact Information for Business Card

R.MOLT ELECTRICAL
Phone: Pernod 0417382554
Pernodm@quellmail.example
EC:47061

```html
<!DOCTYPE html>
<html lang="en">
<head>
<meta charset="utf-8">
<title>R.MOLT ELECTRICAL – Job Card (Back)</title>
<link rel="stylesheet" href="https://fonts.googleapis.com/css2?family=Cabin:ital,wght@1,400&display=swap">
<style>
  :root {
    --cable-black: #151517;
    --cable-dark: #2b2b30;
    --cable-grey: #8f9296;
    --cable-blue: #4d52b0;
    --cable-light: #e4e4e2;
    --copper: #c8694a;
    --frame-red: #e31e25;
    --card-white: #ffffff;
    --ink: #1a1a1a;
  }
  html, body {
    margin: 0;
    padding: 0;
    width: 1200px;
    height: 741px;
    overflow: hidden;
    background: #ffffff;
  }
  .card-back {
    position: relative;
    width: 1200px;
    height: 741px;
    overflow: hidden;
  }
  .cable-backdrop {
    position: absolute;
    inset: 0;
    background:
      radial-gradient(ellipse 230px 160px at 8% 14%, var(--cable-light) 0%, rgba(228,228,226,0) 75%),
      radial-gradient(ellipse 200px 120px at 22% 4%, #f2f2f0 0%, rgba(242,242,240,0) 75%),
      radial-gradient(ellipse 150px 260px at 30% 24%, var(--cable-blue) 0%, rgba(77,82,176,0) 72%),
      radial-gradient(ellipse 170px 90px at 46% 12%, #8088c8 0%, rgba(128,136,200,0) 75%),
      radial-gradient(ellipse 160px 120px at 62% 4%, #9a9ca4 0%, rgba(154,156,164,0) 75%),
      radial-gradient(ellipse 140px 300px at 12% 55%, #7c7f8a 0%, rgba(124,127,138,0) 72%),
      radial-gradient(ellipse 90px 260px at 4% 72%, #6065b8 0%, rgba(96,101,184,0) 72%),
      radial-gradient(ellipse 300px 110px at 14% 80%, #c8c8c6 0%, rgba(200,200,198,0) 72%),
      radial-gradient(ellipse 200px 90px at 34% 97%, #dcdcda 0%, rgba(220,220,218,0) 75%),
      radial-gradient(ellipse 130px 90px at 93% 52%, #6a6fc0 0%, rgba(106,111,192,0) 75%),
      radial-gradient(ellipse 90px 120px at 86% 44%, #b79a7c 0%, rgba(183,154,124,0) 75%),
      radial-gradient(ellipse 230px 120px at 82% 92%, var(--copper) 0%, rgba(200,105,74,0) 72%),
      radial-gradient(ellipse 120px 90px at 84% 98%, #5a5fb0 0%, rgba(90,95,176,0) 75%),
      radial-gradient(ellipse 220px 180px at 85% 20%, var(--cable-black) 0%, rgba(21,21,23,0) 80%),
      radial-gradient(ellipse 220px 200px at 96% 74%, var(--cable-dark) 0%, rgba(43,43,48,0) 80%),
      linear-gradient(135deg, #a8a8ac 0%, #4a4b52 32%, var(--cable-dark) 60%, var(--cable-black) 100%);
  }
  .job-box {
    position: absolute;
    left: 268px;
    top: 208px;
    width: 664px;
    height: 410px;
    box-sizing: border-box;
    border: 15px solid var(--frame-red);
    background: var(--card-white);
  }
  .job-field {
    position: absolute;
    left: 34px;
    right: 35px;
    display: flex;
    align-items: baseline;
    font-family: "Cabin", "Gill Sans", sans-serif;
    font-style: italic;
    font-size: 25px;
    line-height: 1;
    color: var(--ink);
  }
  .job-field .label { white-space: nowrap; }
  .job-field .write-line {
    flex: 1;
    margin-left: 3px;
    border-bottom: 1.2px solid var(--ink);
  }
  .field-time { top: 54px; }
  .field-date { top: 168px; }
  .field-job  { top: 280px; }
</style>
</head>
<body>
  <main class="card-back">
    <div class="cable-backdrop" role="img" aria-label="Photograph of an overwhelming tangle of black, grey, blue and copper electrical cables"></div>
    <section class="job-box">
      <div class="job-field field-time"><span class="label">time:</span><span class="write-line"></span></div>
      <div class="job-field field-date"><span class="label">date:</span><span class="write-line"></span></div>
      <div class="job-field field-job"><span class="label">job description:</span><span class="write-line"></span></div>
    </section>
  </main>
</body>
</html>
```